We need a business card and letterhead design for an orthodontic office. Needs to be clean, simple and sleek

Target Market(s)

adults/children

Industry/Entity Type

Dental

Contact Information for Business Card

Logo that is attached

Font styles to use
Serif

Colors

Designer to choose colors to be used in the design.

Requirements
Must have
• Martin L Okrand DDS
• Corinne Vesta DMD
• 82 Tolliver Avenue
• Dunwick,NY 11874
• (516) 472-9054
• www.okrandortho.example
Nice to have
• on the back.... space for appointment times
Should not have
• teeth

```html
<!DOCTYPE html>
<html lang="en">
<head>
<meta charset="utf-8">
<title>Martin Okrand Orthodontics – Appointment Card</title>
<link rel="stylesheet" href="https://fonts.googleapis.com/css2?family=Josefin+Sans:wght@300&family=Poppins:wght@300;400&display=swap">
<style>
  :root {
    --frame: #3b4347;
    --card: #141718;
    --card-glow: #22272a;
    --white: #ffffff;
    --accent: #5bc2e7;
    --ink: #1c1c1c;
  }
  * { margin: 0; padding: 0; box-sizing: border-box; }
  html, body {
    width: 1200px; height: 720px; overflow: hidden;
    background: var(--frame);
  }
  .card {
    position: absolute; left: 39px; top: 39px;
    width: 1121px; height: 639px;
    background: radial-gradient(ellipse at 55% 30%, var(--card-glow) 0%, var(--card) 70%);
    overflow: hidden;
  }
  .brand {
    position: absolute; left: 0; right: 0; top: 42px;
    text-align: center;
    font-family: "Josefin Sans", sans-serif;
    font-weight: 300;
    color: var(--white);
    line-height: 1;
  }
  .brand-first { display: block; font-size: 86px; letter-spacing: 20px; padding-left: 20px; }
  .brand-last { display: block; font-size: 82px; letter-spacing: 4px; margin-top: 22px; }
  .brand-field { display: block; font-size: 42px; letter-spacing: 2px; margin-top: 22px; }
  .appointment {
    position: absolute; left: 117px; top: 315px;
    width: 893px; height: 240px;
    background: var(--white);
    padding: 9px;
  }
  .appointment-inner {
    width: 100%; height: 100%;
    border: 3px solid var(--accent);
    font-family: "Poppins", sans-serif;
    color: var(--ink);
    padding: 0 30px;
  }
  .appointment-title {
    text-align: center; color: var(--accent);
    font-weight: 400; font-size: 24px; letter-spacing: 1px;
    margin-top: 14px;
  }
  .field-row {
    font-size: 23px; letter-spacing: 1px; white-space: nowrap;
    margin-top: 14px;
  }
  .field-row + .field-row { margin-top: 16px; }
  .blank { letter-spacing: 4.6px; }
  .gap { display: inline-block; width: 18px; }
  .tagline {
    position: absolute; left: 0; right: 0; top: 576px;
    text-align: center;
    font-family: "Poppins", sans-serif; font-weight: 300;
    font-size: 23px; letter-spacing: 1.6px;
    color: var(--white);
  }
  .base-band {
    position: absolute; left: 0; right: 0; bottom: 0;
    height: 15px; background: var(--accent);
  }
</style>
</head>
<body>
  <section class="card">
    <h1 class="brand">
      <span class="brand-first">MARTIN</span>
      <span class="brand-last">OKRAND</span>
      <span class="brand-field">ORTHODONTICS</span>
    </h1>
    <div class="appointment">
      <div class="appointment-inner">
        <h2 class="appointment-title">Next Appointment</h2>
        <p class="field-row">Name: <span class="blank">_______________________________</span></p>
        <p class="field-row">Date: <span class="blank">__/__/____/____</span><span class="gap"></span>Time: <span class="blank">______________</span></p>
      </div>
    </div>
    <p class="tagline">Orthodontics for Children and Adults</p>
    <div class="base-band"></div>
  </section>
</body>
</html>
```